Civora Website

We are a newly formed Real Estate Development Company based in New York. We develop affordable housing apartments. We partner up with private and non profit companies in NY. We would like to have a clean website that relates to our new logo. The target market are individuals that own large parcels of land, churches and private investors and individuals. The final design should communicate financial safety, caring for the community, power and humbleness. Additionally, the website has to be capable to seen in smartphones and the designer has to upload it our hostwren hosting account. The site is going to have around 16 topics. For example: a home page, about us, mission, how we work, our work, building affordable communities, two examples on gentrification, community based planning, Real Estate Consulting, Real Estate Development, Financing/Partnerships, Recruiting, contact page.
See our logo attached.

Target Market(s)

Community leaders, politicians, investors, land owners, activists, real estate brokers, government agencies, other developers,

Industry/Entity Type

Non Profit

Number of Pages Required

1 page

Font styles to use
Sans Serif

Requirements
Must have
• Pictures of buildings from NYC. Facades, lobby, a family in a building, it can be in some cases a combination of sketchers and actual pictures. Clean website.
• People will be able to see it in both desktop and smartphones. The contact page with our information and also to be contacted via email.

```html
<!DOCTYPE html>
<html lang="en">
<head>
<meta charset="utf-8">
<title>Civora – Community Development</title>
<link rel="stylesheet" href="https://fonts.googleapis.com/css2?family=Open+Sans:wght@400;600;700&family=Raleway:wght@300;400&display=swap">
<style>
:root{
  --green:#6cc04a;
  --blue:#1d5fb0;
  --link-blue:#1a6fbd;
  --text:#8a8a8a;
  --heading:#333;
  --light-bg:#f8f8f8;
  --footer-bg:#c3c3c3;
  --bottom-bg:#e6ece4;
  --input-bg:#1c2533;
  --white:#fff;
}
*{margin:0;padding:0;box-sizing:border-box}
html,body{width:924px;height:1200px;overflow:hidden;background:var(--white);font-family:"Open Sans",sans-serif}
.page{position:relative;width:924px;height:1200px}
.abs{position:absolute}

.topbar{left:0;top:0;width:924px;height:30px;border-bottom:1px solid #eee;font-size:9px;color:#999;display:flex;align-items:center;gap:12px;padding-left:45px}
.topbar span{display:flex;align-items:center;gap:4px}

.header{left:0;top:30px;width:924px;height:68px}
.brand{left:50px;top:14px;display:flex;align-items:center;gap:8px;font-family:"Raleway",sans-serif;font-weight:400;font-size:34px;color:var(--blue);letter-spacing:-0.5px}
.brand-mark{width:14px;height:14px;background:var(--green)}
.nav{right:62px;top:22px;display:flex;gap:20px;font-family:"Raleway",sans-serif;font-size:11px;color:#888}
.nav .active{color:var(--green)}

.hero{left:0;top:98px;width:924px;height:380px;background:linear-gradient(180deg,#b9b4a2 0%,#d6d2c2 35%,#6d7275 62%,#8f9796 80%,#d8d7cf 100%)}

.services{left:0;top:478px;width:924px;height:242px;background:var(--light-bg)}
.services-title{left:0;top:480px;width:924px;text-align:center;font-family:"Raleway",sans-serif;font-weight:300;font-size:24px;color:var(--heading)}
.services-sub{left:0;top:519px;width:924px;text-align:center;font-size:10px;color:var(--text)}
.service{width:270px}
.service svg{position:absolute;left:0;top:0}
.service h3{margin-left:40px;font-family:"Raleway",sans-serif;font-weight:400;font-size:16px;line-height:18px;color:var(--heading);text-transform:uppercase}
.service p{margin-left:40px;margin-top:6px;font-size:9.4px;line-height:15px;color:var(--text);width:228px}
.read-more{left:434px;top:671px;width:63px;height:21px;border-bottom:1px solid #ccc;font-size:9.5px;color:#777;text-align:center;line-height:18px}

.gallery{top:720px;height:130px;width:202px}
.photo-1{left:46px;background:linear-gradient(135deg,#c9d6e1,#9fb0be 50%,#b68c72)}
.photo-2{left:256px;background:linear-gradient(180deg,#6f8fb9,#8a7c6a 55%,#6c7a4c)}
.photo-3{left:466px;background:linear-gradient(180deg,#8fb3d1,#b59a80 55%,#4b6f98)}
.photo-4{left:676px;background:linear-gradient(180deg,#3c4f80,#c98e6b 50%,#241d22)}

.footer{left:0;top:864px;width:924px;height:274px;background:var(--footer-bg);border-top:2px solid var(--green)}
.footer-brand{left:62px;top:928px;font-family:"Raleway",sans-serif;font-weight:400;font-size:50px;color:var(--white);letter-spacing:1px}
.footer-info{left:46px;top:996px;font-size:10px;line-height:21.5px;color:var(--link-blue)}
.footer-info div{display:flex;align-items:center;gap:4px}
.footer-info .green{color:#4f9f2d}
.social{left:48px;top:1096px;display:flex;gap:16px}
.social span{width:9px;height:9px;border-radius:50%;background:#8d8d8d}

.newsletter{left:686px;top:902px;width:194px}
.newsletter h4{font-family:"Raleway",sans-serif;font-weight:400;font-size:13px;color:var(--blue)}
.newsletter p{margin-top:8px;font-size:9.5px;line-height:15px;color:var(--link-blue)}
.newsletter label{display:block;margin-top:7px;font-size:9.5px;font-weight:700;color:var(--blue)}
.newsletter .field{height:28px;background:var(--input-bg);margin-top:1px}
.subscribe{display:inline-block;width:65px;height:25px;background:var(--green);color:var(--white);font-size:9.5px;line-height:25px;text-align:center}

.bottombar{left:0;top:1138px;width:924px;height:62px;background:var(--bottom-bg);border-top:1px solid #999}
.copyright{left:45px;top:1157px;font-size:9px;color:#333}
.bottom-nav{right:48px;top:1166px;display:flex;gap:6px;font-size:9px;font-weight:600;color:var(--link-blue)}
.bottom-nav .active{color:var(--green)}
</style>
</head>
<body>
<div class="page">

  <div class="abs topbar">
    <span><svg width="9" height="7" viewBox="0 0 9 7"><rect x="0.5" y="0.5" width="8" height="6" fill="none" stroke="#999"/><path d="M0.5 0.5 4.5 4 8.5 0.5" fill="none" stroke="#999"/></svg>contact@civora.com</span>
    <span><svg width="8" height="8" viewBox="0 0 8 8"><path d="M1 1c0 3 3 6 6 6l1-1.5-2-1-1 1C3.5 4.8 3.2 4.5 2.5 3l1-1-1-2z" fill="#999"/></svg>+1 555-014-2290</span>
  </div>

  <header class="abs header">
    <div class="abs brand"><span class="brand-mark"></span>civora</div>
    <nav class="abs nav">
      <span class="active">Home</span><span>About Us</span><span>Building Affordable Communities</span><span>Gentrification</span><span>Financing/Partnerships</span><span>Blog</span><span>Contact Us</span>
    </nav>
  </header>

  <div class="abs hero" role="img" aria-label="New York skyline with a suspension bridge over the river"></div>

  <section class="abs services"></section>
  <h2 class="abs services-title">Our Services</h2>
  <p class="abs services-sub">We partner up with private and non profit companies in New York.</p>

  <div class="abs service" style="left:46px;top:572px">
    <svg width="18" height="24" viewBox="0 0 18 24"><rect x="1" y="1" width="16" height="22" rx="2" fill="var(--green)"/><rect x="4" y="4" width="10" height="4" fill="#fff"/><g fill="#fff"><rect x="4" y="11" width="2.5" height="2.5"/><rect x="8" y="11" width="2.5" height="2.5"/><rect x="12" y="11" width="2.5" height="2.5"/><rect x="4" y="15" width="2.5" height="2.5"/><rect x="8" y="15" width="2.5" height="2.5"/><rect x="12" y="15" width="2.5" height="2.5"/></g></svg>
    <h3>How We Work</h3>
    <p>Lorem Ipsum is simply dummy text of the printing and typesetting industry. Lorem Ipsum has been the industry's standard dummy text ever since the 1500s, when an unknown printer took a galley.</p>
  </div>
  <div class="abs service" style="left:330px;top:572px">
    <svg width="26" height="22" viewBox="0 0 26 22"><g fill="var(--green)"><circle cx="13" cy="6" r="4"/><circle cx="5" cy="8" r="3"/><circle cx="21" cy="8" r="3"/><path d="M6 20c0-5 3-8 7-8s7 3 7 8z"/><path d="M0 19c0-4 2-6 5-6 1 0 2 .3 2.5.8-1.5 1.4-2.5 3-2.5 5.2z"/><path d="M26 19c0-4-2-6-5-6-1 0-2 .3-2.5.8 1.5 1.4 2.5 3 2.5 5.2z"/></g></svg>
    <h3>Community Based<br>Planning</h3>
    <p>Lorem Ipsum is simply dummy text of the printing and typesetting industry. Lorem Ipsum has been the industry's standard dummy text.</p>
  </div>
  <div class="abs service" style="left:616px;top:572px">
    <svg width="22" height="22" viewBox="0 0 22 22"><path d="M2 9h4v11H2zM8 9l4-7c2 0 3 1 2.5 3L14 8h5c1.5 0 2.5 1.2 2 2.6l-2.2 7.5c-.4 1.2-1.3 1.9-2.5 1.9H8z" fill="none" stroke="var(--green)" stroke-width="2" stroke-linejoin="round"/></svg>
    <h3>Real Estate<br>Development</h3>
    <p>Lorem Ipsum is simply dummy text of the printing and typesetting industry. Lorem Ipsum has been the industry's standard dummy text.</p>
  </div>
  <div class="abs read-more">read more</div>

  <div class="abs gallery photo-1" role="img" aria-label="Couple laughing by the river with city towers behind"></div>
  <div class="abs gallery photo-2" role="img" aria-label="People walking on an elevated park walkway among new buildings"></div>
  <div class="abs gallery photo-3" role="img" aria-label="Multi-generation family smiling together by the harbor"></div>
  <div class="abs gallery photo-4" role="img" aria-label="City skyline at dusk with a lit tower"></div>

  <footer class="abs footer"></footer>
  <div class="abs footer-brand">civora</div>
  <div class="abs footer-info">
    <div>&nbsp;Civora - Community Development</div>
    <div><svg width="7" height="10" viewBox="0 0 7 10"><path d="M3.5 0A3.5 3.5 0 0 0 0 3.5C0 6 3.5 10 3.5 10S7 6 7 3.5A3.5 3.5 0 0 0 3.5 0zm0 5a1.5 1.5 0 1 1 0-3 1.5 1.5 0 0 1 0 3z" fill="var(--link-blue)"/></svg>212 Harlow Ave - New York, NY 10027</div>
    <div><svg width="9" height="7" viewBox="0 0 9 7"><rect x="0.5" y="0.5" width="8" height="6" fill="none" stroke="var(--link-blue)"/><path d="M0.5 0.5 4.5 4 8.5 0.5" fill="none" stroke="var(--link-blue)"/></svg>Email: <span class="green">contact@civora.com</span></div>
    <div><svg width="8" height="8" viewBox="0 0 8 8"><path d="M1 1c0 3 3 6 6 6l1-1.5-2-1-1 1C3.5 4.8 3.2 4.5 2.5 3l1-1-1-2z" fill="var(--link-blue)"/></svg>Phone: +1 555-014-2290</div>
  </div>
  <div class="abs social"><span></span><span></span><span></span><span></span><span></span><span></span></div>

  <div class="abs newsletter">
    <h4>Newsletter</h4>
    <p>Sign up to receive news and promotions in your email.</p>
    <label>Name:</label>
    <div class="field"></div>
    <label>E-mail:</label>
    <div class="field"></div>
    <span class="subscribe">Subscribe</span>
  </div>

  <div class="abs bottombar"></div>
  <div class="abs copyright">Copyright © 2015 Harbor Row Collective. All Rights Reserved.</div>
  <nav class="abs bottom-nav">
    <span class="active">Home</span><span>About Us</span><span>Building Affordable Communities</span><span>Gentrification</span><span>Financing/Partnerships</span><span>Blog</span><span>Contact Us</span>
  </nav>

</div>
</body>
</html>
```